Plant your Garden - Landing Page Visual

Looking to polish up this visual. This will be a landing page for a career progression site that employees use to see what is required to promote from one position to another. We want to stick to a Nautical theme. Each of the icons will be used to hyperlink to another page. The design needs to use our Colors as you see in the Tolvin logo attachment. The RGB color for the orange is 255,67,16. The design needs to use a nautical compass and have a swooping upward ribbon or arrow effect. The files need to be given is AI format as each of the icons need to be transferred as a separate Vector file as well.

```html
<!DOCTYPE html>
<html lang="en">
<head>
<meta charset="utf-8">
<title>Plant your Garden – Career Path</title>
<link rel="stylesheet" href="https://fonts.googleapis.com/css2?family=Questrial&family=Raleway:wght@500;600&display=swap">
<style>
  :root {
    --orange: #ff4310;
    --navy: #1c1f2b;
    --ink: #111111;
    --paper: #ffffff;
    --compass-light: #f1f1f1;
    --compass-mid: #c9c9c9;
    --compass-dark: #3a3a3a;
  }
  * { margin: 0; padding: 0; box-sizing: border-box; }
  html, body { width: 1200px; height: 1059px; overflow: hidden; background: var(--paper); }
  .canvas { position: relative; width: 1200px; height: 1059px; font-family: "Questrial", sans-serif; }
  .variant { position: absolute; left: 0; width: 1200px; }
  .variant--labels { top: 0; height: 527px; }
  .variant--ribbons { top: 540px; height: 519px; }
  .divider { position: absolute; left: 0; top: 527px; width: 1200px; height: 13px; background: var(--navy); }

  .brand { position: absolute; display: flex; align-items: center; gap: 8px;
    font-family: "Raleway", sans-serif; font-weight: 600; font-size: 28px; color: var(--ink); letter-spacing: 1px; }
  .brand__mark { width: 18px; height: 18px; background: var(--orange); }

  .headline { position: absolute; line-height: 1; font-weight: 400; }
  .headline__small { display: block; font-size: 42px; color: var(--ink); letter-spacing: 4px; }
  .headline__large { display: block; font-size: 112px; color: var(--orange); letter-spacing: -1px; margin-top: -4px; }
  .variant--ribbons .headline__small { letter-spacing: 9px; font-size: 38px; margin-left: 70px; }
  .variant--ribbons .headline__large { font-size: 104px; }

  .compass { position: absolute; border-radius: 50%;
    background: radial-gradient(circle, var(--compass-dark) 0 4%, var(--compass-mid) 5% 12%,
      var(--compass-light) 13% 44%, var(--compass-mid) 45% 48%, var(--compass-light) 49% 60%,
      rgba(255,255,255,0) 66%); }

  .route { position: absolute; left: 0; top: 0; width: 1200px; height: 100%; }

  .step-label { position: absolute; font-family: "Raleway", sans-serif; font-weight: 500;
    font-size: 21px; line-height: 29px; color: var(--orange); letter-spacing: 1px; }
  .step-tab { position: absolute; height: 28px; display: flex; align-items: center; padding-left: 12px;
    font-family: "Raleway", sans-serif; font-weight: 600; font-size: 18px; color: var(--paper); white-space: nowrap; }
</style>
</head>
<body>
<main class="canvas">

  <svg width="0" height="0" style="position:absolute" aria-hidden="true">
    <defs>
      <symbol id="icon-forklift" viewBox="-25 -25 50 50">
        <path d="M-16,-20 V14 M-16,10 H-24" stroke="#fff" stroke-width="3" fill="none"/>
        <rect x="-12" y="-2" width="26" height="13" rx="2" fill="#fff"/>
        <path d="M-8,-2 V-16 H8 L12,-2" stroke="#fff" stroke-width="3" fill="none"/>
        <circle cx="-6" cy="14" r="5" fill="#ff4310"/>
        <circle cx="10" cy="14" r="5" fill="#ff4310"/>
      </symbol>
      <symbol id="icon-truck" viewBox="-25 -25 50 50">
        <rect x="-22" y="-14" width="26" height="24" rx="2" fill="#fff"/>
        <path d="M6,-6 H14 L21,4 V10 H6 Z" fill="#fff"/>
        <rect x="9" y="-3" width="6" height="6" fill="#111"/>
        <circle cx="-12" cy="12" r="5" fill="#ff4310"/>
        <circle cx="12" cy="12" r="5" fill="#ff4310"/>
      </symbol>
      <symbol id="icon-clipboard" viewBox="-25 -25 50 50">
        <rect x="-15" y="-17" width="30" height="37" rx="3" fill="none" stroke="#fff" stroke-width="3"/>
        <rect x="-7" y="-22" width="14" height="8" rx="2" fill="#ff4310"/>
        <path d="M-9,-6 H9 M-9,2 H9 M-9,10 H3" stroke="#fff" stroke-width="3"/>
        <rect x="6" y="6" width="5" height="10" fill="#ff4310"/>
      </symbol>
      <symbol id="icon-gear" viewBox="-25 -25 50 50">
        <circle r="15" fill="none" stroke="#fff" stroke-width="7" stroke-dasharray="5.9 5.9"/>
        <circle r="12" fill="none" stroke="#fff" stroke-width="4"/>
        <circle r="5" fill="#ff4310"/>
      </symbol>
      <symbol id="icon-stopwatch" viewBox="-25 -25 50 50">
        <circle cy="3" r="17" fill="none" stroke="#fff" stroke-width="3.5"/>
        <rect x="-4" y="-21" width="8" height="6" rx="1" fill="#ff4310"/>
        <path d="M0,3 V-8 M0,3 L8,8" stroke="#ff4310" stroke-width="3" stroke-linecap="round"/>
      </symbol>
    </defs>
  </svg>

  <section class="variant variant--labels">
    <div class="brand" style="left:19px; top:22px;"><span class="brand__mark"></span>Tolvin</div>
    <h1 class="headline" style="left:184px; top:80px;">
      <span class="headline__small" style="margin-left:76px;">Plant your</span>
      <span class="headline__large">Garden</span>
    </h1>
    <div class="compass" role="img" aria-label="Nautical compass rose with north, east, south and west points" style="left:128px; top:280px; width:290px; height:240px;"></div>

    <svg class="route" viewBox="0 0 1200 527" aria-hidden="true">
      <polyline points="273,357 513,391" fill="none" stroke="var(--navy)" stroke-width="6"/>
      <polyline points="524,400 600,330 650,328 718,262 765,258 840,190 880,186 950,112 985,106 1028,36"
        fill="none" stroke="var(--navy)" stroke-width="5"/>
      <polygon points="1036,24 1008,38 1024,50" fill="var(--navy)"/>
      <g stroke="var(--orange)" stroke-width="4" fill="var(--ink)">
        <circle cx="524" cy="429" r="42"><title>Equipment Operator</title></circle>
        <circle cx="629" cy="353" r="42"><title>Delivery Driver</title></circle>
        <circle cx="740" cy="280" r="42"><title>Warehouse Specialist</title></circle>
        <circle cx="853" cy="203" r="42"><title>Training Specialist</title></circle>
        <circle cx="957" cy="127" r="42"><title>Spec Lead Delivery</title></circle>
      </g>
      <use href="#icon-forklift" x="496" y="401" width="56" height="56"/>
      <use href="#icon-truck" x="601" y="325" width="56" height="56"/>
      <use href="#icon-clipboard" x="712" y="252" width="56" height="56"/>
      <use href="#icon-gear" x="825" y="175" width="56" height="56"/>
      <use href="#icon-stopwatch" x="929" y="99" width="56" height="56"/>
    </svg>

    <div class="step-label" style="left:578px; top:412px;">Equipment<br>Operator</div>
    <div class="step-label" style="left:688px; top:343px; letter-spacing:4px;">Delivery<br>Driver</div>
    <div class="step-label" style="left:800px; top:266px;">Warehouse<br>Specialist</div>
    <div class="step-label" style="left:909px; top:190px; letter-spacing:2px;">Training<br>Specialist</div>
    <div class="step-label" style="left:1019px; top:115px;">Spec Lead<br>Delivery</div>
  </section>

  <div class="divider"></div>

  <section class="variant variant--ribbons">
    <div class="brand" style="left:19px; top:24px;"><span class="brand__mark"></span>Tolvin</div>
    <h1 class="headline" style="left:140px; top:96px;">
      <span class="headline__small">Plant your</span>
      <span class="headline__large">Garden</span>
    </h1>
    <div class="compass" role="img" aria-label="Nautical compass rose with north, east, south and west points" style="left:98px; top:270px; width:260px; height:230px;"></div>

    <svg class="route" viewBox="0 0 1200 519" aria-hidden="true">
      <polyline points="228,333 440,370" fill="none" stroke="var(--navy)" stroke-width="6"/>
      <polyline points="453,372 525,305 565,302 630,240 668,236 735,170 778,166 835,102 870,98 925,30"
        fill="none" stroke="var(--navy)" stroke-width="5"/>
      <polygon points="934,20 906,33 921,46" fill="var(--navy)"/>
      <g fill="var(--orange)" stroke="var(--navy)" stroke-width="2">
        <polygon points="490,397 705,397 715,412 705,427 490,427"/>
        <polygon points="597,324 805,324 815,339 805,354 597,354"/>
        <polygon points="700,255 912,255 922,269 912,283 700,283"/>
        <polygon points="806,177 1012,177 1022,190 1012,204 806,204"/>
        <polygon points="906,103 1123,103 1133,116 1123,129 906,129"/>
      </g>
      <g stroke="var(--orange)" stroke-width="4" fill="var(--ink)">
        <circle cx="453" cy="407" r="42"><title>Equipment Operator</title></circle>
        <circle cx="560" cy="333" r="42"><title>Delivery Driver</title></circle>
        <circle cx="663" cy="260" r="42"><title>Warehouse Specialist</title></circle>
        <circle cx="773" cy="183" r="42"><title>Training Specialist</title></circle>
        <circle cx="869" cy="113" r="42"><title>Spec Lead Delivery</title></circle>
      </g>
      <use href="#icon-forklift" x="425" y="379" width="56" height="56"/>
      <use href="#icon-truck" x="532" y="305" width="56" height="56"/>
      <use href="#icon-clipboard" x="635" y="232" width="56" height="56"/>
      <use href="#icon-gear" x="745" y="155" width="56" height="56"/>
      <use href="#icon-stopwatch" x="841" y="85" width="56" height="56"/>
    </svg>

    <div class="step-tab" style="left:497px; top:398px;">Equipment Operator</div>
    <div class="step-tab" style="left:604px; top:325px; letter-spacing:3px;">Delivery Driver</div>
    <div class="step-tab" style="left:707px; top:255px;">Warehouse Specialist</div>
    <div class="step-tab" style="left:815px; top:177px;">Training Specialist</div>
    <div class="step-tab" style="left:913px; top:102px;">Spec Lead Delivery</div>
  </section>

</main>
</body>
</html>
```